parts and kits

we need an updated flyer to email to our customers
we need to have what we sell at kivo
caliper pistons
seal kits
new brake cylinders
brake boosters
brake shoes
brake pads
brake hoses
cables -accelerator, clutch, hand brake etc
for both private, vintage and commercial vehicles

```html
<!DOCTYPE html>
<html lang="en">
<head>
<meta charset="utf-8">
<title>Kivo Auto Centre – Parts and Kits Flyer</title>
<link href="https://fonts.googleapis.com/css2?family=Montserrat:ital,wght@0,500;0,600;0,700;1,700&display=swap" rel="stylesheet">
<style>
  :root{
    --yellow:#fdd439;
    --black:#0d0d0d;
    --ink:#1c1c1c;
    --white:#ffffff;
    --paper:#f1f2f3;
    --page:#e4e4e4;
    --steel-dark:#3d3f42;
    --steel-mid:#7b7e82;
    --steel-light:#c9cbcd;
  }
  *{box-sizing:border-box;margin:0;padding:0}
  html,body{width:1200px;height:1200px;overflow:hidden;background:var(--page)}
  body{font-family:"Montserrat",Arial,sans-serif;color:var(--ink)}
  .flyer{position:absolute;left:176px;top:0;width:848px;height:1200px;background:var(--paper);overflow:hidden}
  .hero{position:absolute;left:0;top:0;width:848px;height:554px;display:block}
  .brand{position:absolute;left:600px;top:300px;width:230px;text-align:center;font-weight:700;color:var(--ink);line-height:1.05}
  .brand-name{display:block;font-size:56px;letter-spacing:.04em}
  .brand-sub{display:block;font-size:19px;margin-top:10px;letter-spacing:.02em}
  .headline{position:absolute;left:0;top:498px;width:848px;text-align:center;font-size:29px;font-weight:700;line-height:33px;color:var(--ink)}
  .offer{position:absolute;left:0;top:599px;width:848px;height:243px;background:var(--black)}
  .offer-tab{position:absolute;left:271px;top:-19px;width:265px;height:40px;background:var(--yellow);clip-path:polygon(8% 0,100% 0,92% 100%,0 100%);display:flex;align-items:center;justify-content:center;font-size:25px;font-weight:700;color:var(--ink)}
  .offer-divider{position:absolute;left:404px;top:37px;width:1.5px;height:192px;background:var(--white)}
  .offer-list{position:absolute;top:34px;list-style:none;color:var(--white);font-size:21px;font-weight:500;line-height:32.6px}
  .offer-list.left{left:82px}
  .offer-list.right{left:482px}
  .offer-list li{position:relative;padding-left:21px}
  .offer-list li svg{position:absolute;left:0;top:11px;width:12px;height:12px}
  .offer-list .cont{padding-left:21px}
  .vehicles{position:absolute;left:0;top:842px;width:848px;height:45px;background:var(--yellow);text-align:center;font-size:28px;font-weight:600;line-height:45px;color:var(--ink)}
  .products{position:absolute;left:32px;top:904px;display:flex;gap:10px}
  .product{width:122px;height:122px;border:1.5px solid #333;background:var(--white);padding:8px}
  .product span{display:block;width:100%;height:100%;background:radial-gradient(circle at 50% 50%,#6b6d70 0%,#9b9ea1 45%,#eceded 75%)}
  .aim{position:absolute;left:0;top:1038px;width:848px;text-align:center;font-size:24px;font-style:italic;font-weight:700;line-height:31px;color:var(--ink)}
  .contact{position:absolute;left:0;top:1109px;width:848px;height:91px;background:var(--yellow)}
  .contact-phone{position:absolute;left:0;top:0;width:347px;height:91px;background:var(--black);clip-path:polygon(0 0,315px 0,347px 100%,0 100%);display:flex;align-items:center;padding-left:32px;color:var(--white);font-size:31px;font-weight:700;letter-spacing:.02em}
  .contact-phone svg{width:32px;height:32px;margin-right:15px}
  .contact-web{position:absolute;left:413px;top:16px;font-size:19px;font-weight:500;letter-spacing:.13em;line-height:32px;color:var(--ink)}
  .contact-web div{display:flex;align-items:center}
  .contact-web svg{width:18px;height:18px;margin-right:10px}
</style>
</head>
<body>
<main class="flyer">
  <svg class="hero" viewBox="0 0 1224 800" preserveAspectRatio="none">
    <defs>
      <linearGradient id="steel" x1="0" y1="0" x2="1" y2="1">
        <stop offset="0" stop-color="#5a5c5f"/>
        <stop offset=".45" stop-color="#a7a9ab"/>
        <stop offset=".75" stop-color="#6c6e71"/>
        <stop offset="1" stop-color="#3a3b3d"/>
      </linearGradient>
    </defs>
    <rect x="0" y="0" width="1224" height="800" fill="#f1f2f3"/>
    <polygon role="img" aria-label="Photo of re-manufactured brake callipers on a workshop bench" points="0,0 1224,0 1224,178 700,520 0,490" fill="url(#steel)"/>
    <polygon points="0,490 200,585 0,525" fill="#fdd439"/>
    <polygon points="1224,178 700,520 1224,780" fill="#fdd439"/>
  </svg>

  <div class="brand">
    <span class="brand-name">KIVO</span>
    <span class="brand-sub">KIVO AUTO CENTRE</span>
  </div>

  <h1 class="headline">Specialise in the Re-Manufacture of<br>Brakes, Hoses and Cables</h1>

  <section class="offer">
    <div class="offer-tab">What We Sell</div>
    <ul class="offer-list left">
      <li><svg viewBox="0 0 12 12"><path d="M1 6.5 4.5 10 11 2" fill="none" stroke="#fff" stroke-width="2"/></svg>Caliper Pistons</li>
      <li><svg viewBox="0 0 12 12"><path d="M1 6.5 4.5 10 11 2" fill="none" stroke="#fff" stroke-width="2"/></svg>Seal Kits</li>
      <li><svg viewBox="0 0 12 12"><path d="M1 6.5 4.5 10 11 2" fill="none" stroke="#fff" stroke-width="2"/></svg>New Brake Cylinders</li>
      <li><svg viewBox="0 0 12 12"><path d="M1 6.5 4.5 10 11 2" fill="none" stroke="#fff" stroke-width="2"/></svg>Brake Boosters</li>
      <li><svg viewBox="0 0 12 12"><path d="M1 6.5 4.5 10 11 2" fill="none" stroke="#fff" stroke-width="2"/></svg>Brake Shoes</li>
      <li><svg viewBox="0 0 12 12"><path d="M1 6.5 4.5 10 11 2" fill="none" stroke="#fff" stroke-width="2"/></svg>Boosters</li>
    </ul>
    <div class="offer-divider"></div>
    <ul class="offer-list right">
      <li><svg viewBox="0 0 12 12"><path d="M1 6.5 4.5 10 11 2" fill="none" stroke="#fff" stroke-width="2"/></svg>Brake pads</li>
      <li><svg viewBox="0 0 12 12"><path d="M1 6.5 4.5 10 11 2" fill="none" stroke="#fff" stroke-width="2"/></svg>Brake hoses</li>
      <li><svg viewBox="0 0 12 12"><path d="M1 6.5 4.5 10 11 2" fill="none" stroke="#fff" stroke-width="2"/></svg>Cables - accelerator,</li>
      <li class="cont">clutch, hand brake</li>
      <li><svg viewBox="0 0 12 12"><path d="M1 6.5 4.5 10 11 2" fill="none" stroke="#fff" stroke-width="2"/></svg>Rubber &amp; Braided Hoses</li>
      <li><svg viewBox="0 0 12 12"><path d="M1 6.5 4.5 10 11 2" fill="none" stroke="#fff" stroke-width="2"/></svg>Source Brake Parts</li>
    </ul>
  </section>

  <div class="vehicles">Parts for motor bikes, cars, commercial etc</div>

  <div class="products">
    <div class="product"><span role="img" aria-label="Product photo: brake shoes"></span></div>
    <div class="product"><span role="img" aria-label="Product photo: brake pads"></span></div>
    <div class="product"><span role="img" aria-label="Product photo: seal kit"></span></div>
    <div class="product"><span role="img" aria-label="Product photo: caliper piston"></span></div>
    <div class="product"><span role="img" aria-label="Product photo: brake master cylinder"></span></div>
    <div class="product"><span role="img" aria-label="Product photo: brake booster"></span></div>
  </div>

  <p class="aim">Our aim is to repair parts with the quickest<br>turn-around times possible</p>

  <footer class="contact">
    <div class="contact-phone">
      <svg viewBox="0 0 24 24"><path fill="#fff" d="M6.6 10.8a15.1 15.1 0 0 0 6.6 6.6l2.2-2.2c.3-.3.7-.4 1-.2 1.1.4 2.3.6 3.6.6.6 0 1 .4 1 1V20c0 .6-.4 1-1 1A17 17 0 0 1 3 4c0-.6.4-1 1-1h3.5c.6 0 1 .4 1 1 0 1.3.2 2.5.6 3.6.1.3 0 .7-.2 1z"/></svg>
      0800 555 018
    </div>
    <div class="contact-web">
      <div><svg viewBox="0 0 24 24"><path fill="#1c1c1c" d="M2 5h20v14H2z"/><path d="M2 5l10 8 10-8" fill="none" stroke="#fdd439" stroke-width="2"/></svg>parts@kivoautocentre.co.nz</div>
      <div><svg viewBox="0 0 24 24"><g fill="none" stroke="#1c1c1c" stroke-width="2"><circle cx="12" cy="12" r="10"/><ellipse cx="12" cy="12" rx="4" ry="10"/><path d="M2 12h20M4 7h16M4 17h16"/></g></svg>www.kivoautocentre.co.nz</div>
    </div>
  </footer>
</main>
</body>
</html>
```